Business Card - Cooperate

Business Card for Larkfield Management Consulting

Target Market(s)

Corparte - b2B

Industry/Entity Type

Management Consulting - Professional Services

Contact Information for Business Card

Company Name , Slogan , Dummy Address,

Requirements
Must have
• Reach your Full Potential

```html
<!DOCTYPE html>
<html lang="en">
<head>
<meta charset="utf-8">
<title>Larkfield Management Consulting – Business Card</title>
<link rel="stylesheet" href="https://fonts.googleapis.com/css2?family=Questrial&family=Ubuntu:wght@500&display=swap">
<style>
  :root {
    --backdrop: #e6e7ea;
    --paper: #ffffff;
    --paper-shade: #f1f1f1;
    --brand-blue: #2a55ad;
    --teal: #17a08a;
    --ink: #2b2b2b;
    --back-light: #2b62b4;
    --back-mid: #224392;
    --back-dark: #1d1c5e;
    --back-text: #2f68c4;
    --back-note: #c9d3ec;
  }
  * { box-sizing: border-box; margin: 0; padding: 0; }
  html, body { width: 1200px; height: 732px; overflow: hidden; }
  body {
    background: var(--backdrop);
    position: relative;
    font-family: "Questrial", sans-serif;
  }
  .card {
    position: absolute;
    top: 206px;
    width: 560px;
    height: 320px;
    overflow: hidden;
    box-shadow: 0 6px 18px rgba(0,0,0,0.18);
  }
  .card--front {
    left: 25px;
    background: linear-gradient(160deg, var(--paper) 0%, var(--paper) 45%, var(--paper-shade) 100%);
  }
  .card--back {
    left: 615px;
    background: radial-gradient(ellipse 62% 75% at 60% 50%, var(--back-light) 0%, var(--back-mid) 55%, var(--back-dark) 100%);
  }

  .brand {
    position: absolute;
    left: 22px;
    top: 26px;
    display: flex;
    align-items: center;
    gap: 12px;
  }
  .brand__dot {
    width: 52px; height: 52px; border-radius: 50%;
    background: var(--brand-blue);
  }
  .brand__name {
    font-size: 46px;
    line-height: 1;
    color: var(--brand-blue);
  }

  .person {
    position: absolute;
    right: 20px;
    top: 164px;
    text-align: right;
  }
  .person__name {
    font-family: "Ubuntu", sans-serif;
    font-weight: 500;
    font-size: 25px;
    line-height: 1.1;
    color: var(--brand-blue);
  }
  .person__role {
    font-size: 16px;
    color: var(--ink);
    line-height: 1.1;
  }

  .rule { position: absolute; top: 225px; height: 1.5px; }
  .rule--blue { left: 21px; width: 266px; background: var(--brand-blue); }
  .rule--teal { left: 293px; width: 248px; background: var(--teal); }

  .address {
    position: absolute;
    left: 22px;
    top: 263px;
    font-style: normal;
    font-size: 16px;
    line-height: 1.2;
    color: var(--ink);
  }
  .contacts {
    position: absolute;
    right: 18px;
    top: 245px;
    list-style: none;
    font-size: 16px;
    line-height: 1.2;
    color: var(--ink);
  }
  .contacts li {
    display: flex;
    justify-content: flex-end;
    align-items: center;
    gap: 10px;
  }
  .contacts svg { width: 14px; height: 14px; flex: none; }

  .back-brand {
    position: absolute;
    left: 150px;
    right: 0;
    top: 118px;
    text-align: center;
  }
  .back-brand__name {
    font-size: 60px;
    line-height: 1;
    color: var(--back-text);
  }
  .back-note {
    position: absolute;
    left: 150px;
    right: 0;
    bottom: 34px;
    text-align: center;
    font-size: 16px;
    color: var(--back-note);
  }
</style>
</head>
<body>
  <section class="card card--front" aria-label="Business card front">
    <div class="brand">
      <span class="brand__dot"></span>
      <span class="brand__name">larkfield</span>
    </div>

    <div class="person">
      <p class="person__name">Daniel Hart</p>
      <p class="person__role">Owner/ CEO</p>
    </div>

    <span class="rule rule--blue"></span>
    <span class="rule rule--teal"></span>

    <address class="address">
      0/00 Mercer Lane<br>Brookvale, 0000
    </address>

    <ul class="contacts">
      <li>09. 5550. 0142
        <svg viewBox="0 0 16 16" aria-hidden="true"><path d="M3.5 1.5l2.5 3-1.5 1.5c.8 2 2.5 3.7 4.5 4.5l1.5-1.5 3 2.5-1.5 2.5C7 14 2 9 1 3z" fill="none" stroke="#17a08a" stroke-width="1.5" stroke-linejoin="round"/></svg>
      </li>
      <li>09. 5550. 0142
        <svg viewBox="0 0 16 16" aria-hidden="true"><rect x="4" y="1" width="8" height="14" rx="1.5" fill="none" stroke="#17a08a" stroke-width="1.5"/><circle cx="8" cy="12.5" r="0.9" fill="#17a08a"/></svg>
      </li>
      <li>hart@larkfield.com
        <svg viewBox="0 0 16 16" aria-hidden="true"><rect x="1" y="3" width="14" height="10" fill="#17a08a"/><path d="M1 3l7 6 7-6M1 13l5-5M15 13l-5-5" fill="none" stroke="#fff" stroke-width="1.1"/></svg>
      </li>
    </ul>
  </section>

  <section class="card card--back" aria-label="Business card back">
    <div class="back-brand">
      <p class="back-brand__name">larkfield</p>
    </div>
    <p class="back-note">Reach your full potential</p>
  </section>
</body>
</html>
```